We are a building company that build new homes and units we are looking for something fresh and looks good my company name is
Larkmoor Building Group Pty Ltd

Industry/Entity Type

Building

Contact Information for Business Card

Name Marco Delacruz-Fenn
Tittle: Director
Address 14 Quarrel St. Thornbury Vic 3071
Ph: 03 9612 4087
Mobile : 0400 562 938

www.larkmoorbuildinggroup.com.au
Email: sales@larkmoorbuildinggroup.com.au

```html
<!DOCTYPE html>
<html lang="en">
<head>
<meta charset="utf-8">
<title>Larkmoor Building Group – Business Card</title>
<link href="https://fonts.googleapis.com/css2?family=Oswald:wght@300;500&family=Ubuntu+Condensed&family=Kalam:wght@400&display=swap" rel="stylesheet">
<style>
  :root {
    --charcoal: #414141;
    --brand-blue: #00aaeb;
    --blue-deep: #0b86b8;
    --white: #ffffff;
    --page: #ffffff;
  }
  * { box-sizing: border-box; margin: 0; padding: 0; }
  html, body {
    width: 993px; height: 1200px; overflow: hidden;
    background: var(--page);
  }
  .sheet { position: relative; width: 993px; height: 1200px; }

  .card {
    position: absolute; left: 55px; width: 881px; height: 546px;
    background: var(--charcoal); overflow: hidden;
    box-shadow: 0 2px 8px rgba(0,0,0,0.45);
  }
  .card--front { top: 47px; }
  .card--back { top: 611px; }

  /* Front */
  .brand {
    position: absolute; left: 0; right: 0; top: 190px;
    display: flex; align-items: center; justify-content: center; gap: 22px;
  }
  .brand__mark { width: 46px; height: 46px; background: var(--brand-blue); }
  .brand__name {
    font-family: "Oswald", sans-serif; font-weight: 500;
    font-size: 52px; letter-spacing: 3px; text-transform: uppercase;
    color: var(--white); line-height: 1;
  }
  .front-rule {
    position: absolute; left: 0; right: 0; top: 446px; height: 15px;
    background: var(--white);
  }
  .front-band {
    position: absolute; left: 0; right: 0; top: 461px; bottom: 0;
    background: linear-gradient(to bottom, var(--blue-deep) 0%, var(--brand-blue) 35%, var(--brand-blue) 100%);
    display: flex; align-items: center; justify-content: center;
  }
  .front-band__tagline {
    font-family: "Kalam", cursive; font-size: 30px; color: var(--white);
    padding-top: 4px;
  }

  /* Back */
  .side-strip { position: absolute; left: 0; top: 0; width: 154px; height: 100%; }
  .side-shadow {
    position: absolute; left: 154px; top: 0; width: 12px; height: 100%;
    background: linear-gradient(to right, rgba(0,0,0,0.5), rgba(0,0,0,0));
  }
  .contact { position: absolute; left: 219px; top: 100px; width: 640px; }
  .contact__name {
    font-family: "Oswald", sans-serif; font-weight: 500; font-size: 40px;
    color: var(--white); letter-spacing: 0.5px; line-height: 1;
  }
  .contact__rule {
    margin-top: 14px; height: 3px; width: 631px;
    background: linear-gradient(to right, #ffffff 0%, #dddddd 60%, rgba(255,255,255,0) 100%);
  }
  .contact__list { list-style: none; margin-top: 20px; }
  .contact__item {
    display: flex; align-items: center; gap: 20px; height: 44px;
    color: var(--white);
  }
  .contact__item svg { width: 36px; height: 32px; flex: none; }
  .contact__item--phone { font-family: "Oswald", sans-serif; font-weight: 300; font-size: 30px; letter-spacing: 1px; }
  .contact__item--online { font-family: "Ubuntu Condensed", sans-serif; font-size: 28px; height: 42px; }
  .contact__item--gap { margin-top: 24px; }
  .back-tagline {
    position: absolute; left: 214px; top: 462px;
    font-family: "Kalam", cursive; font-size: 31px; color: var(--white);
  }
</style>
</head>
<body>
<main class="sheet">
  <section class="card card--front">
    <div class="brand">
      <span class="brand__mark"></span>
      <span class="brand__name">Larkmoor Building Group</span>
    </div>
    <div class="front-rule"></div>
    <div class="front-band">
      <p class="front-band__tagline">New home design and construction</p>
    </div>
  </section>

  <section class="card card--back">
    <svg class="side-strip" viewBox="0 0 154 546" preserveAspectRatio="none">
      <rect width="154" height="546" fill="var(--brand-blue)"/>
      <polygon points="0,546 154,440 154,546" fill="var(--white)"/>
    </svg>
    <div class="side-shadow"></div>

    <div class="contact">
      <h1 class="contact__name">MARCO DELACRUZ-FENN</h1>
      <div class="contact__rule"></div>
      <ul class="contact__list">
        <li class="contact__item contact__item--phone">
          <svg viewBox="0 0 36 32" fill="none" stroke="#fff" stroke-width="2" stroke-linejoin="round">
            <path d="M8 3 l5 0 l2 7 l-3 3 q3 7 10 11 l3-3 l7 2 l0 5 q-1 2-4 2 Q10 29 5 7 q0-3 3-4z"/>
          </svg>
          <span>03 9612 4087</span>
        </li>
        <li class="contact__item contact__item--phone">
          <svg viewBox="0 0 36 32" fill="none" stroke="#fff" stroke-width="2">
            <rect x="10" y="2" width="16" height="28" rx="2"/>
            <line x1="10" y1="6" x2="26" y2="6"/>
            <line x1="10" y1="24" x2="26" y2="24"/>
            <circle cx="18" cy="27" r="1" fill="#fff"/>
          </svg>
          <span>0400 562 938</span>
        </li>
        <li class="contact__item contact__item--online contact__item--gap">
          <svg viewBox="0 0 36 32" fill="none" stroke="#fff" stroke-width="2">
            <rect x="6" y="6" width="24" height="16" rx="1"/>
            <path d="M2 26 h32 l-2 3 h-28z" fill="#fff"/>
          </svg>
          <span>www.larkmoorbuildinggroup.com.au</span>
        </li>
        <li class="contact__item contact__item--online">
          <svg viewBox="0 0 36 32" fill="none" stroke="#fff" stroke-width="2">
            <rect x="3" y="7" width="30" height="19"/>
            <path d="M3 7 l15 11 l15-11 M3 26 l11-10 M33 26 l-11-10"/>
          </svg>
          <span>sales@larkmoorbuildinggroup.com.au</span>
        </li>
      </ul>
    </div>
    <p class="back-tagline">Quality, excellence and innovation</p>
  </section>
</main>
</body>
</html>
```